Cedar Lantern Roots Gathering Music Conference & Concert Series needs a banner design to welco...

We are looking for a banner to use as a backdrop where people can take pictures and promote the event as they upload to social media. The music conference primarily targets high school students so we are looking for a design that will attract a younger audience. The festival revolves around music appreciation in the US/Mexico border. We like the "Cedar LanternRoots Gathering" trumpet logo on the "5th annual" design attached, but we are open to other designs.
Target Market(s)
ages 15-45
Colors
Designer to choose colors to be used in the design.
Look and feel

```html
<!DOCTYPE html>
<html lang="en">
<head>
<meta charset="utf-8">
<title>Cedar Lantern Roots Gathering — 5th Annual</title>
<link rel="stylesheet" href="https://fonts.googleapis.com/css2?family=Playfair+Display:wght@700&family=Oswald:wght@400&family=Montserrat:wght@500&family=Cormorant+Garamond:ital,wght@1,600&display=swap">
<style>
  :root {
    --ink: #ffffff;
    --rule: #f2a88e;
    --deep: #2a0f22;
    --crimson: #8e2040;
    --magenta: #9a2f78;
    --violet: #7a3aa0;
    --shadow: #1a0a1c;
  }
  html, body {
    margin: 0;
    padding: 0;
    width: 1200px;
    height: 960px;
    overflow: hidden;
    background: var(--deep);
  }
  .banner {
    position: relative;
    width: 1200px;
    height: 960px;
    overflow: hidden;
    color: var(--ink);
    text-align: center;
  }
  .crowd-backdrop {
    position: absolute;
    inset: 0;
    background:
      radial-gradient(ellipse 60% 45% at 20% 75%, rgba(214, 70, 110, 0.55), transparent 70%),
      radial-gradient(ellipse 55% 50% at 85% 55%, rgba(168, 80, 200, 0.55), transparent 70%),
      linear-gradient(180deg, #3a1024 0%, var(--crimson) 40%, var(--magenta) 62%, var(--shadow) 100%),
      linear-gradient(90deg, var(--crimson), var(--violet));
    background-blend-mode: screen, screen, normal, normal;
  }
  .crowd-backdrop::after {
    content: "";
    position: absolute;
    inset: 0;
    background: linear-gradient(180deg, rgba(20, 6, 20, 0.45) 0%, rgba(20, 6, 20, 0) 45%, rgba(20, 6, 20, 0.55) 100%);
  }
  .content {
    position: absolute;
    inset: 0;
    z-index: 1;
  }
  .edition {
    position: absolute;
    left: 0;
    right: 0;
    top: 124px;
    margin: 0;
    font-family: "Playfair Display", Georgia, serif;
    font-weight: 700;
    line-height: 1;
  }
  .edition .ordinal {
    display: block;
    font-size: 54px;
  }
  .edition .annual {
    display: block;
    font-size: 70px;
    margin-top: 10px;
    letter-spacing: 1px;
  }
  .rule {
    position: absolute;
    left: 380px;
    width: 440px;
    height: 3px;
    background: var(--rule);
  }
  .rule-top { top: 295px; }
  .rule-bottom { top: 656px; }
  .event-name {
    margin: 0;
    font-weight: normal;
  }
  .event-name .primary,
  .event-name .secondary {
    position: absolute;
    left: 0;
    right: 0;
    white-space: nowrap;
    line-height: 1;
    text-transform: uppercase;
  }
  .event-name .primary {
    top: 334px;
    font-family: "Oswald", "Arial Narrow", sans-serif;
    font-weight: 400;
    font-size: 158px;
    letter-spacing: 1px;
  }
  .event-name .secondary {
    top: 536px;
    font-family: "Montserrat", Arial, sans-serif;
    font-weight: 500;
    font-size: 74px;
    letter-spacing: 8px;
  }
  .tagline {
    position: absolute;
    left: 0;
    right: 0;
    top: 700px;
    margin: 0;
    font-family: "Cormorant Garamond", Georgia, serif;
    font-style: italic;
    font-weight: 600;
    font-size: 38px;
    line-height: 1.2;
    white-space: nowrap;
  }
</style>
</head>
<body>
  <main class="banner">
    <div class="crowd-backdrop" role="img" aria-label="Concert crowd with raised hands in silhouette against red and purple stage haze"></div>
    <div class="content">
      <p class="edition"><span class="ordinal">5TH</span><span class="annual">ANNUAL</span></p>
      <div class="rule rule-top"></div>
      <h1 class="event-name">
        <span class="primary">Cedar Lantern</span>
        <span class="secondary">Roots Gathering</span>
      </h1>
      <div class="rule rule-bottom"></div>
      <p class="tagline">Music conference &amp; Concert series</p>
    </div>
  </main>
</body>
</html>
```